Velnor Group: Business Card for a high end technology company

We need a cool new design for our business cards using our cloud logo. We are a technology consulting business. We pride ourselves on be the best of the best. We mainly focus on cloud solutions and managed services. We need a business card that sets us apart from the other technology companies in the area and allows us to stand out.

Target Market(s)

Technology departments, CIO, CEOs, and Information Technology Staff.

Industry/Entity Type

Information Technology

Contact Information for Business Card

Must have the logo and our name.
Must have employee name, email address, office phone, cell phone and website.
Need to have all info on one side a cool design on backside.

Font styles to use
Serif
Sans Serif

Requirements
Must have
• Must have the logo and our name.
• Must have employee name, email address, office phone, cell phone and website.
• Need to have all info on one side a cool design on back side.
• Must be a crisp clean design, not too busy or confusing.

```html
<!DOCTYPE html>
<html lang="en">
<head>
<meta charset="utf-8">
<title>Velnor Group — Business Card</title>
<link rel="stylesheet" href="https://fonts.googleapis.com/css2?family=Questrial&family=Arimo:wght@400;700&display=swap">
<style>
  :root {
    --stage: #e9eaec;
    --card-top: #ffffff;
    --card-bottom: #ececec;
    --ink: #3a3a3a;
    --ink-soft: #5a5a5a;
    --blue: #2f8fd8;
    --blue-deep: #1f6fb8;
    --blue-light: #5fb0ea;
    --divider: #c9c9c9;
  }
  * { box-sizing: border-box; margin: 0; padding: 0; }
  html, body { width: 1200px; height: 950px; overflow: hidden; }
  body {
    background: var(--stage);
    font-family: "Arimo", Arial, sans-serif;
    position: relative;
  }
  .card {
    position: absolute;
    left: 250px;
    width: 700px;
    height: 400px;
    background: linear-gradient(160deg, var(--card-top) 0%, var(--card-top) 45%, var(--card-bottom) 100%);
    box-shadow: 0 2px 10px rgba(0,0,0,.12);
    overflow: hidden;
  }
  .card--back { top: 45px; }
  .card--front { top: 495px; }

  .brand {
    display: flex;
    flex-direction: column;
    align-items: center;
  }
  .brand__row { display: flex; align-items: center; gap: 14px; }
  .brand__dot {
    width: 34px; height: 34px; border-radius: 50%;
    background: var(--blue);
  }
  .brand__name {
    font-family: "Questrial", "Century Gothic", sans-serif;
    color: var(--ink);
    font-size: 44px;
    letter-spacing: .5px;
  }
  .brand__url {
    margin-top: 4px;
    font-family: "Arimo", Arial, sans-serif;
    font-weight: 700;
    font-size: 12px;
    color: var(--ink);
  }
  .card--back .brand {
    position: absolute; left: 0; right: 0; top: 160px;
  }
  .card--back .brand__name { font-size: 52px; }
  .card--back .brand__dot { width: 40px; height: 40px; }
  .card--back .brand__url { font-size: 14px; }

  .card--front .brand {
    position: absolute; left: 40px; width: 300px; top: 135px;
  }
  .divider {
    position: absolute; left: 368px; top: 85px;
    width: 1px; height: 190px;
    background: linear-gradient(to bottom, transparent, var(--divider) 20%, var(--divider) 80%, transparent);
  }
  .contact {
    position: absolute; left: 395px; top: 95px;
  }
  .contact__name {
    font-weight: 700; font-size: 24px; color: var(--blue);
  }
  .contact__role {
    font-size: 17px; color: var(--ink); margin-top: 2px; margin-bottom: 16px;
  }
  .contact__line {
    display: flex; align-items: center; gap: 10px;
    font-size: 17px; color: var(--ink-soft); line-height: 25px;
  }
  .contact__line svg { width: 14px; height: 14px; fill: var(--blue-deep); flex: none; }

  .band {
    position: absolute; left: 0; right: 0; top: 300px; height: 40px;
    background: linear-gradient(to right, var(--blue-deep), var(--blue) 50%, var(--blue-light));
    display: flex; align-items: center; padding-left: 55px;
  }
  .band__url {
    color: #ffffff; font-size: 16px; letter-spacing: 5px;
  }
</style>
</head>
<body>

  <section class="card card--back" aria-label="Card back">
    <div class="brand">
      <div class="brand__row">
        <span class="brand__dot"></span>
        <span class="brand__name">Velnor Group</span>
      </div>
      <span class="brand__url">www.velnorgroup.com</span>
    </div>
  </section>

  <section class="card card--front" aria-label="Card front">
    <div class="brand">
      <div class="brand__row">
        <span class="brand__dot"></span>
        <span class="brand__name">Velnor Group</span>
      </div>
      <span class="brand__url">www.velnorgroup.com</span>
    </div>

    <div class="divider"></div>

    <div class="contact">
      <p class="contact__name">Marcus Hale</p>
      <p class="contact__role">President</p>
      <p class="contact__line">
        <svg viewBox="0 0 16 16" aria-hidden="true"><path d="M3 1h3l1.5 4-2 1.3a9 9 0 0 0 4.2 4.2L11 8.5l4 1.5v3a2 2 0 0 1-2 2A13 13 0 0 1 1 3a2 2 0 0 1 2-2z"/></svg>
        412 5580 1936
      </p>
      <p class="contact__line">
        <svg viewBox="0 0 16 16" aria-hidden="true"><path d="M4 0h8a1 1 0 0 1 1 1v14a1 1 0 0 1-1 1H4a1 1 0 0 1-1-1V1a1 1 0 0 1 1-1zm1 2v10h6V2zm3 11a1 1 0 1 0 0 2 1 1 0 0 0 0-2z"/></svg>
        734 2091 6648
      </p>
      <p class="contact__line">
        <svg viewBox="0 0 16 16" aria-hidden="true"><path d="M0 3h16v10H0zm1.5 1.2V5l6.5 4 6.5-4v-.8z"/></svg>
        marcus@velnorgroup.com
      </p>
    </div>

    <div class="band">
      <span class="band__url">www.velnor.com</span>
    </div>
  </section>

</body>
</html>
```